Figma App design and working prototype

I need to create a User Interface design and a Working prototype using Figma or similar. I’d also like all the assets and guidelines needed to guide the App developers to create the final product.
So, I'll need Design files and assets but you that I can give to an App development company or a freelance developer to create Android and iOS apps.

This app is an app for adults who wan to meet and have sex no strings attached.

The App name will be Nuvora

I have attached an app some pictures and a pdf file explaining details of the apps functions.

This app will be a sexy version of the pobalo app with a personals section used for adult services. I have attached images and a pdf below that will tell you the functions of the app.

I need an app interface design done for an app idea I have. I am nee to this it is my first time trying to launch an app and I do not know what you need in order to get what I need. I need a site map/ design and if possible a working prototype that I can pass on to an app developer that can deliver the final product. This model will be used to raise funds and give investors an idea of what the apps functions will do as detailed in the project brief. Any advise would be greatly appreciated. Please let me know if you have any questions. Looking forward to working with you.

Target Market(s)

Adults men and women looking for some adult entertainment

Industry/Entity Type

Adult entertainment Strip clubs

Colors
E54698
E96AAD
F1A4CE
F9D9EA
FCEFF6
A7469A
B969AE
D3A5CF
EDDBEB
F8F0F9
6B429C
8869AF
B7A5CE
E3DAEB
F3F0F8

Requirements
Must have
• An 18+ confirmation,
Nice to have
• A sexy feel.

```html
<!DOCTYPE html>
<html lang="en">
<head>
<meta charset="utf-8">
<title>Nuvora – App Screens</title>
<link rel="stylesheet" href="https://fonts.googleapis.com/css2?family=Poppins:wght@400;500;600;700&display=swap">
<style>
  :root {
    --canvas: #d6a5a5;
    --plum-deep: #36084a;
    --plum-mid: #4a1450;
    --rose: #e96aad;
    --orchid: #b85c99;
    --lilac: #b39acb;
    --lilac-soft: #b7a5ce;
    --magenta: #a0138e;
    --magenta-soft: #b75ea5;
    --icon-bg: #f1dcec;
    --icon-ink: #8e2d8c;
    --heading-pink: #b0508f;
    --surface: #ffffff;
    --surface-muted: #f4f4f4;
    --ink: #1e1e1e;
    --ink-soft: #6f6f6f;
    --verified: #8a1fd6;
    --online: #2fcf6a;
  }
  * { box-sizing: border-box; margin: 0; padding: 0; }
  html, body { width: 1023px; height: 1200px; overflow: hidden; }
  body { background: var(--canvas); font-family: "Poppins", sans-serif; position: relative; }

  .screen { position: absolute; top: 105px; width: 366px; height: 791px; overflow: hidden; }

  /* Age gate */
  .age-gate { left: 113px; background: var(--plum-deep); }
  .age-gate__hero {
    position: absolute; inset: 0;
    background: linear-gradient(180deg, #2a1a17 0%, #4a2a24 30%, #5a2a3e 55%, #3e0c4c 75%, var(--plum-deep) 100%);
  }
  .brand { position: absolute; top: 278px; left: 0; right: 0; display: flex; flex-direction: column; align-items: center; gap: 6px; }
  .brand__dot { width: 58px; height: 58px; border-radius: 50%; border: 7px solid #e7c7ea; }
  .brand__name { color: var(--rose); font-weight: 500; font-size: 41px; letter-spacing: 1px; }
  .age-gate__question { position: absolute; top: 484px; width: 100%; text-align: center; color: #fff; font-size: 16px; }
  .btn { position: absolute; left: 71px; width: 223px; height: 41px; border: 0; color: #fff; font-family: inherit; font-size: 16px; display: flex; align-items: center; justify-content: center; }
  .btn--yes { top: 556px; background: var(--orchid); }
  .btn--no { top: 624px; background: var(--lilac); }

  /* Home */
  .home { left: 536px; width: 374px; background: var(--surface-muted); }
  .status-bar { position: absolute; top: 0; left: 0; right: 0; height: 89px; background: var(--orchid); border-radius: 0 0 24px 24px; color: #fff; z-index: 2; }
  .status-bar__time { position: absolute; left: 17px; top: 22px; font-size: 14px; }
  .status-bar__icons { position: absolute; right: 17px; top: 25px; }
  .top-area { position: absolute; top: 0; left: 0; right: 0; height: 244px; background: var(--surface); box-shadow: 0 1px 3px rgba(0,0,0,.08); }
  .search { position: absolute; top: 105px; left: 17px; width: 341px; height: 61px; border-radius: 31px; background: #fff; box-shadow: 0 2px 8px rgba(0,0,0,.12); display: flex; align-items: center; }
  .search__sort { margin-left: 17px; }
  .search__placeholder { margin-left: 24px; color: #7a7a7a; font-size: 14px; flex: 1; }
  .search__btn { width: 44px; height: 44px; border-radius: 50%; background: var(--lilac-soft); margin-right: 12px; display: flex; align-items: center; justify-content: center; }
  .categories { position: absolute; top: 184px; left: 0; right: 0; }
  .category { position: absolute; width: 80px; margin-left: -40px; text-align: center; font-size: 9px; color: #333; }
  .category__icon { width: 42px; height: 42px; border-radius: 50%; background: var(--icon-bg); margin: 0 auto 7px; display: flex; align-items: center; justify-content: center; }

  .promo { position: absolute; top: 281px; left: 17px; width: 340px; height: 234px; border-radius: 8px; background: linear-gradient(180deg, var(--magenta) 0%, var(--magenta-soft) 100%); overflow: hidden; }
  .promo__title { position: absolute; left: 17px; top: 20px; color: #fff; font-weight: 600; font-size: 18px; line-height: 24px; }
  .promo__slide { position: absolute; top: 96px; height: 101px; }
  .promo__slide--main { left: 14px; width: 215px; background: linear-gradient(135deg, #3a2630 0%, #d04fa6 60%, #f07ac4 100%); }
  .promo__slide--next { left: 240px; width: 100px; background: linear-gradient(135deg, #c89a86 0%, #6b4a40 100%); }
  .promo__dots { position: absolute; top: 217px; left: 0; right: 0; display: flex; justify-content: center; gap: 6px; }
  .promo__dots span { width: 5px; height: 5px; border-radius: 50%; background: #fff; }

  .section-head { position: absolute; top: 541px; left: 18px; right: 18px; display: flex; justify-content: space-between; align-items: center; }
  .section-head__title { color: var(--heading-pink); font-weight: 500; font-size: 14px; }
  .filter { display: flex; align-items: center; gap: 5px; font-size: 10px; color: #222; }
  .toggle { width: 32px; height: 14px; border-radius: 7px; background: #ddd; position: relative; margin-left: 6px; }
  .toggle::after { content: ""; position: absolute; right: -2px; top: -2px; width: 18px; height: 18px; border-radius: 50%; background: #9a9a9a; }

  .listing { position: absolute; width: 160px; height: 179px; background: #fff; box-shadow: 0 1px 3px rgba(0,0,0,.12); overflow: hidden; }
  .listing__photo { height: 110px; position: relative; }
  .listing__badge { position: absolute; top: 0; right: 0; }
  .listing__online { position: absolute; right: 6px; bottom: 6px; background: var(--online); color: #fff; font-size: 5px; padding: 2px 5px; border-radius: 6px; }
  .listing__title { padding: 6px 4px 0; font-size: 8.5px; font-weight: 500; line-height: 12.5px; color: var(--ink); height: 36px; }
  .listing__meta { display: flex; justify-content: space-between; padding: 4px 4px 0; font-size: 7.5px; line-height: 11px; color: #222; }
  .listing__meta .right { text-align: right; padding-top: 2px; }
</style>
</head>
<body>

<section class="screen age-gate">
  <div class="age-gate__hero" role="img" aria-label="Photo of an embracing couple in low, warm light"></div>
  <div class="brand">
    <div class="brand__dot"></div>
    <div class="brand__name">Nuvora</div>
  </div>
  <p class="age-gate__question">Are you 18+ years old?</p>
  <div class="btn btn--yes">Yes, let me in</div>
  <div class="btn btn--no">No, get me out of here</div>
</section>

<section class="screen home">
  <div class="top-area"></div>
  <header class="status-bar">
    <span class="status-bar__time">04:20</span>
    <svg class="status-bar__icons" width="74" height="14" viewBox="0 0 74 14">
      <rect x="0" y="9" width="3" height="4" fill="#fff"/><rect x="5" y="7" width="3" height="6" fill="#fff"/><rect x="10" y="4" width="3" height="9" fill="#fff"/><rect x="15" y="1" width="3" height="12" fill="#fff"/>
      <path d="M25 5 a10 10 0 0 1 14 0 M28 8 a6 6 0 0 1 8 0" stroke="#fff" stroke-width="2" fill="none"/><circle cx="32" cy="11" r="1.6" fill="#fff"/>
      <rect x="46" y="1" width="25" height="12" rx="2" fill="none" stroke="#fff" stroke-width="1.5"/><rect x="48.5" y="3.5" width="20" height="7" fill="#fff"/><rect x="72" y="5" width="2" height="4" fill="#fff"/>
    </svg>
  </header>

  <div class="search">
    <svg class="search__sort" width="12" height="18" viewBox="0 0 12 18"><path d="M6 0 L12 7 H0Z M6 18 L0 11 H12Z" fill="#b39acb"/></svg>
    <span class="search__placeholder">Type anything here</span>
    <div class="search__btn">
      <svg width="22" height="22" viewBox="0 0 22 22"><circle cx="10" cy="10" r="8" stroke="#fff" stroke-width="2" fill="none"/><line x1="16" y1="16" x2="21" y2="21" stroke="#fff" stroke-width="2"/></svg>
    </div>
  </div>

  <nav class="categories">
    <div class="category" style="left:38px"><div class="category__icon"><svg width="20" height="24" viewBox="0 0 20 24"><circle cx="9" cy="4" r="3.5" fill="var(--icon-ink)"/><path d="M5 9 h8 l4 14 H2Z" fill="var(--icon-ink)"/></svg></div>Escorts</div>
    <div class="category" style="left:107px"><div class="category__icon"><svg width="14" height="28" viewBox="0 0 14 28"><rect x="1" y="1" width="12" height="26" rx="6" fill="var(--icon-ink)"/><circle cx="7" cy="8" r="2.5" fill="#fff"/><rect x="5.5" y="15" width="3" height="7" rx="1.5" fill="#fff"/></svg></div>Sex Toys</div>
    <div class="category" style="left:181px"><div class="category__icon"><svg width="26" height="24" viewBox="0 0 26 24"><path d="M2 2 L8 8 H18 L24 2 V14 A11 10 0 0 1 2 14Z" fill="var(--icon-ink)"/><circle cx="13" cy="14" r="4" fill="#fff"/></svg></div>Virtual Escorts</div>
    <div class="category" style="left:254px"><div class="category__icon"><svg width="24" height="28" viewBox="0 0 24 28"><path d="M3 1 L9 16 H15 L21 1 V18 A9 9 0 0 1 3 18Z" fill="var(--icon-ink)"/><circle cx="12" cy="20" r="3" fill="#fff"/></svg></div>Party</div>
    <div class="category" style="left:327px"><div class="category__icon"><svg width="24" height="24" viewBox="0 0 24 24" fill="none" stroke="var(--icon-ink)" stroke-width="1.8"><circle cx="6" cy="6" r="4.5"/><circle cx="18" cy="6" r="4.5"/><circle cx="6" cy="18" r="4.5"/><circle cx="18" cy="18" r="4.5"/></svg></div>All Categories</div>
  </nav>

  <section class="promo">
    <h2 class="promo__title">Whatever pleasure you desire,<br>we can satify you.</h2>
    <div class="promo__slide promo__slide--main" role="img" aria-label="Featured top models promotional photo"></div>
    <div class="promo__slide promo__slide--next" role="img" aria-label="Next promotional photo"></div>
    <div class="promo__dots"><span></span><span></span><span></span><span></span><span></span></div>
  </section>

  <div class="section-head">
    <h3 class="section-head__title">Trending Female Escorts</h3>
    <div class="filter">
      <svg width="11" height="11" viewBox="0 0 11 11"><circle cx="5.5" cy="5.5" r="5.5" fill="var(--orchid)"/><path d="M3 5.6 L4.8 7.3 L8 3.8" stroke="#fff" stroke-width="1.4" fill="none"/></svg>
      Verified <span class="toggle"></span>
    </div>
  </div>

  <article class="listing" style="left:18px; top:576px">
    <div class="listing__photo" role="img" aria-label="Listing photo of a woman in lilac lingerie" style="background:linear-gradient(135deg,#c8b6c4,#8d6aa5 60%,#efe7ee)">
      <svg class="listing__badge" width="28" height="34" viewBox="0 0 28 34"><path d="M0 0 H28 V34Z" fill="var(--verified)"/><circle cx="17" cy="11" r="6" fill="#fff"/><path d="M14 11 L16.2 13 L20 9" stroke="var(--verified)" stroke-width="1.6" fill="none"/></svg>
    </div>
    <p class="listing__title">LAST DAY IN HUNTSVILLE<br>Marisol Sexy&amp;Milf</p>
    <div class="listing__meta"><div>Hourly Rate<br>$250/hr</div><div class="right">Posted:<br>19 mins ago</div></div>
  </article>

  <article class="listing" style="left:196px; top:576px">
    <div class="listing__photo" role="img" aria-label="Listing photo of a woman in a pink outfit" style="background:linear-gradient(135deg,#7a6a62,#ea4fa6 45%,#f06bb3 70%,#5a4a44)">
      <svg class="listing__badge" width="28" height="34" viewBox="0 0 28 34"><path d="M0 0 H28 V34Z" fill="var(--verified)"/><circle cx="17" cy="11" r="6" fill="#fff"/><path d="M14 11 L16.2 13 L20 9" stroke="var(--verified)" stroke-width="1.6" fill="none"/></svg>
      <span class="listing__online">● Online now</span>
    </div>
    <p class="listing__title">Super Hot Party Girl. ***~Jolie~***<br>Hotel guest welcome</p>
    <div class="listing__meta"><div>Hourly Rate<br>$250/hr</div><div class="right">Posted:<br>19 mins ago</div></div>
  </article>

  <article class="listing" style="left:18px; top:768px">
    <div class="listing__photo" role="img" aria-label="Listing photo" style="background:linear-gradient(135deg,#b07a5a,#d9b8a0 60%,#cfe3c8)">
      <svg class="listing__badge" width="28" height="34" viewBox="0 0 28 34"><path d="M0 0 H28 V34Z" fill="var(--verified)"/><circle cx="17" cy="11" r="6" fill="#fff"/><path d="M14 11 L16.2 13 L20 9" stroke="var(--verified)" stroke-width="1.6" fill="none"/></svg>
    </div>
  </article>

  <article class="listing" style="left:196px; top:768px">
    <div class="listing__photo" role="img" aria-label="Listing photo" style="background:linear-gradient(135deg,#5a5a5a,#c9a98e 60%,#ffffff)">
      <svg class="listing__badge" width="28" height="34" viewBox="0 0 28 34"><path d="M0 0 H28 V34Z" fill="var(--verified)"/><circle cx="17" cy="11" r="6" fill="#fff"/><path d="M14 11 L16.2 13 L20 9" stroke="var(--verified)" stroke-width="1.6" fill="none"/></svg>
    </div>
  </article>
</section>

</body>
</html>
```